Design new Brackwater Asset business card 2016

We need a new business card for our company Brackwater Asset Partners. We are a niche Alternative Investment Fund Manager based in Chester, in the North West of the UK.We market our services to global institutions such as banks, insurance companies, pension funds, etc. as well as wealthy individuals. Our main markets are Europe (Germany\France\Switzerland), the US and parts of Asia.
The design needs to be in line with existing company branding. Life the assets we deal with, the business card might suggest, "niche\alternative" type of attributes - however, it needs to remain professional, clean and appropriate for our client base.
Our existing business card format with relevant factual information is included, along with logo and branding details.

Target Market(s)

We market our services to global institutions such as banks, insurance companies, pension funds, etc. as well as wealthy individuals.

Industry/Entity Type

Financial Service

Contact Information for Business Card

please see attached pdf for information on existing business card which we should aim to convey on your new design. However:
- the wording "Brackwater Asset Partners Ltd is Authorised and Regulated
by the Monetary Oversight Bureau. Registered No. 7139046" should be replaced with , "Brackwater Asset Partners Ltd is an Alternative Investment Fund Manager Authorised and Regulated by the Monetary Oversight Bureau. Registered No. 7139046"
- the "reception" word on reverse can be omitted.
- the "retail: www.toplivanex.co.uk" wording can be omitted.
- the QR code is not required in the new version.

Font styles to use
Serif
Sans Serif

Requirements
Must have
• information on current business card, subject to comments provided above.
Nice to have
• Use of areas of solid colour instead of large areas of white space might be nice to experiment with. However, still need to have the general look and feel of the brand as presented on our website www.bwfundco.co.uk
• If we had space for 3 bullet points describing what we do\who we are, this might be good to try out. e.g. alternative investment fund manager, longevity specialist, founded 1990.
• Also, we have a new tag line, "expertise with longevity" which might fit nicely somewhere on the business card.
Should not have
• - no QR code
• - should not use all the colours in our logo as it looks very garish! Using one or two colours with black\white etc, seems to work better.

```html
<!DOCTYPE html>
<html lang="en">
<head>
<meta charset="utf-8">
<title>Brackwater Asset Partners – Business Card</title>
<link rel="stylesheet" href="https://fonts.googleapis.com/css2?family=Arimo:wght@400;700&family=Libre+Baskerville&display=swap">
<style>
  :root {
    --page: #e4e2df;
    --paper: #ffffff;
    --brown: #6e3c07;
    --gold: #c9a227;
    --gold-deep: #a8882a;
    --ink: #3b3b3b;
    --white: #ffffff;
  }
  * { box-sizing: border-box; margin: 0; padding: 0; }
  html, body { width: 1200px; height: 950px; overflow: hidden; }
  body {
    background: var(--page);
    font-family: "Arimo", Arial, sans-serif;
    display: flex; flex-direction: column; align-items: center; justify-content: center;
    gap: 50px;
  }
  .card {
    position: relative; width: 700px; height: 400px;
    background: var(--paper); overflow: hidden;
    box-shadow: 0 6px 18px rgba(0,0,0,.18);
  }

  /* Front */
  .card-front { text-align: center; color: var(--ink); }
  .front-mark {
    position: absolute; top: 58px; left: 0; right: 0;
    display: flex; flex-direction: column; align-items: center; gap: 16px;
  }
  .mark-dot { width: 96px; height: 96px; border-radius: 50%; background: var(--brown); }
  .brand-name {
    font-family: "Libre Baskerville", Georgia, serif; font-weight: 400;
    color: var(--brown); font-size: 24px; letter-spacing: .5px;
  }
  .front-bullets { position: absolute; top: 268px; left: 0; right: 0; font-size: 14.5px; }
  .front-rule { position: absolute; top: 293px; left: 140px; right: 140px; height: 1px; background: var(--gold); }
  .front-legal { position: absolute; top: 305px; left: 0; right: 0; font-size: 13px; line-height: 1.5; }

  /* Back */
  .card-back { background: var(--brown); color: var(--white); }
  .back-shape { position: absolute; inset: 0; }
  .back-brand {
    position: absolute; left: 370px; top: 90px; width: 320px;
    display: flex; flex-direction: column; align-items: center; gap: 14px;
  }
  .back-brand .mark-dot { width: 62px; height: 62px; }
  .back-brand .brand-name { font-size: 21px; }
  .holder { position: absolute; left: 48px; top: 112px; }
  .holder-name { color: var(--gold); font-weight: 700; font-size: 22px; }
  .holder-role { font-size: 16px; margin-top: 4px; }
  .contact-list { position: absolute; left: 48px; top: 262px; list-style: none; font-size: 15px; }
  .contact-list li { display: flex; align-items: center; gap: 10px; height: 21px; }
  .contact-list svg { width: 14px; height: 14px; fill: var(--gold); }
  .tagline { position: absolute; left: 48px; top: 355px; font-weight: 700; font-size: 16px; }
</style>
</head>
<body>

<section class="card card-front" aria-label="Card front">
  <div class="front-mark">
    <span class="mark-dot"></span>
    <span class="brand-name">Brackwater Asset Partners</span>
  </div>
  <p class="front-bullets">Alternative Investment Fund Manager • Longevity Specialist • Founded 1990</p>
  <div class="front-rule"></div>
  <p class="front-legal">Brackwater Asset Partners Ltd is an Alternative Investment Fund Manager Authorised<br>and Regulated by the Monetary Oversight Bureau. Registered No. 7139046</p>
</section>

<section class="card card-back" aria-label="Card back">
  <svg class="back-shape" viewBox="0 0 700 400" aria-hidden="true">
    <circle cx="560" cy="70" r="262" fill="none" stroke="var(--gold)" stroke-width="4"/>
    <circle cx="560" cy="70" r="254" fill="var(--paper)"/>
  </svg>
  <div class="back-brand">
    <span class="mark-dot"></span>
    <span class="brand-name">Brackwater Asset Partners</span>
  </div>
  <div class="holder">
    <p class="holder-name">Owen Hartley</p>
    <p class="holder-role">Non-Executive Chairman</p>
  </div>
  <ul class="contact-list">
    <li><svg viewBox="0 0 14 14"><path d="M1 4c0-2 2-3 6-3s6 1 6 3l-3 1-1-2H5L4 5zM3 6h8l2 7H1z"/></svg>+44 (0)1632 960418</li>
    <li><svg viewBox="0 0 14 14"><path d="M4 0h6a1 1 0 011 1v12a1 1 0 01-1 1H4a1 1 0 01-1-1V1a1 1 0 011-1zm1 2v9h4V2z"/></svg>+44 (0)7700 900527</li>
    <li><svg viewBox="0 0 14 14"><path d="M0 3h14v8H0zM1 4l6 4 6-4v-.5H1z" fill-rule="evenodd"/></svg>ohartley@bwfundco.co.uk</li>
    <li><svg viewBox="0 0 14 14"><circle cx="7" cy="7" r="6.5"/><path d="M1 7h12M7 .5v13" stroke="#6e3c07" stroke-width="1"/></svg>www.bwfundco.co.uk</li>
  </ul>
  <p class="tagline">Expertise with longevity</p>
</section>

</body>
</html>
```